One business card required with 2 company logos and 2 people's details

One business card required.
No preference on design - One side could show the 2 different business logos for the companies we own. The reverse could have the details shown below.
Another option could be one business one side and one business on the reverse. Happy to receive designs.

Carol Denbigh
07700 318 274
Rachel Tolland
07700 582 036

website: truelymarvellous.example
email: info@truelymarvellous.example

website: ironwillowevents.example
email: info:ironwillowevents.example

May be nice to have icons instead of the words email/website?

I have included different versions of the logos to help with your design.

Contact Information for Business Card

see project overview

Requirements
Must have
• both company logos, both contact names and contact details

```html
<!DOCTYPE html>
<html lang="en">
<head>
<meta charset="utf-8">
<title>Business Card – Truely Marvellous &amp; Iron Willow Events</title>
<link href="https://fonts.googleapis.com/css2?family=Montserrat:wght@400;500;700;800&display=swap" rel="stylesheet">
<style>
  :root {
    --backdrop: #d9d9d7;
    --card: #ffffff;
    --navy: #2f3060;
    --band-navy: #3a3b66;
    --blue: #3a7fc8;
    --bright-blue: #2f6fc0;
    --ink: #333;
  }
  * { box-sizing: border-box; margin: 0; padding: 0; }
  html, body { width: 1200px; height: 801px; overflow: hidden; }
  body {
    background: var(--backdrop);
    font-family: "Montserrat", sans-serif;
    display: flex; align-items: center; justify-content: center; gap: 50px;
  }
  .card {
    position: relative; width: 545px; height: 352px;
    background: var(--card); overflow: hidden;
    box-shadow: 0 6px 18px rgba(0,0,0,.18);
  }

  /* brand marks as plain text */
  .brand { display: flex; align-items: center; gap: 8px; font-weight: 700; }
  .brand .dot { border-radius: 50%; flex: none; }
  .brand--marvellous { color: var(--navy); }
  .brand--marvellous .dot { background: var(--navy); }
  .brand--willow { color: var(--bright-blue); }
  .brand--willow .dot { background: var(--bright-blue); }

  /* front */
  .front .brand--marvellous { position: absolute; left: 34px; top: 96px; font-size: 19px; }
  .front .brand--marvellous .dot { width: 14px; height: 14px; }
  .front .brand--willow { position: absolute; right: 40px; top: 30px; font-size: 17px; }
  .front .brand--willow .dot { width: 12px; height: 12px; }

  .person { position: absolute; font-size: 12.5px; color: var(--ink); line-height: 1.55; }
  .person .name { font-weight: 800; font-size: 21px; letter-spacing: .5px; line-height: 1.2; margin-bottom: 3px; }
  .person .row { display: flex; align-items: center; gap: 7px; }
  .person .row svg { width: 11px; height: 11px; flex: none; }

  .person--carol { left: 30px; top: 180px; }
  .person--carol .name { color: var(--navy); }
  .person--carol svg { fill: var(--navy); }

  .person--rachel { right: 32px; top: 98px; text-align: right; }
  .person--rachel .name { color: var(--blue); }
  .person--rachel .row { justify-content: flex-end; }
  .person--rachel svg { fill: var(--blue); }

  .band {
    position: absolute; height: 34px; color: #fff; font-size: 13.5px;
    display: flex; align-items: center; gap: 8px;
  }
  .band svg { width: 12px; height: 12px; fill: #fff; flex: none; }
  .band--marvellous {
    left: 0; bottom: 14px; width: 300px; background: var(--blue);
    padding-left: 28px; clip-path: polygon(0 0, 100% 0, calc(100% - 16px) 100%, 0 100%);
  }
  .band--willow {
    right: 0; bottom: 28px; width: 255px; background: var(--band-navy);
    padding-left: 30px; justify-content: flex-start;
    clip-path: polygon(16px 0, 100% 0, 100% 100%, 0 100%);
  }
  .band--willow svg { margin-left: 6px; }

  /* back */
  .back .divider {
    position: absolute; left: 50%; top: 82px; width: 1.5px; height: 188px; background: var(--blue);
  }
  .back .brand { position: absolute; top: 50%; transform: translateY(-50%); font-size: 21px; }
  .back .brand .dot { width: 16px; height: 16px; }
  .back .brand--marvellous { left: 36px; }
  .back .brand--willow { right: 30px; }
</style>
</head>
<body>
  <section class="card front" aria-label="Card front with contact details">
    <div class="brand brand--willow"><span class="dot"></span>Iron Willow Events</div>
    <div class="brand brand--marvellous"><span class="dot"></span>Truely Marvellous</div>

    <div class="person person--rachel">
      <div class="name">RACHEL TOLLAND</div>
      <div class="row">07700 582 036
        <svg viewBox="0 0 24 24"><path d="M6.6 10.8a15 15 0 0 0 6.6 6.6l2.2-2.2c.3-.3.7-.4 1-.2 1.1.4 2.3.6 3.6.6.6 0 1 .4 1 1V20c0 .6-.4 1-1 1A17 17 0 0 1 3 4c0-.6.4-1 1-1h3.5c.6 0 1 .4 1 1 0 1.3.2 2.5.6 3.6.1.3 0 .7-.2 1z"/></svg></div>
      <div class="row">info:ironwillowevents.example
        <svg viewBox="0 0 24 24"><path d="M2 5h20v14H2z M2 5l10 8 10-8" /></svg></div>
    </div>

    <div class="person person--carol">
      <div class="name">CAROL DENBIGH</div>
      <div class="row"><svg viewBox="0 0 24 24"><path d="M6.6 10.8a15 15 0 0 0 6.6 6.6l2.2-2.2c.3-.3.7-.4 1-.2 1.1.4 2.3.6 3.6.6.6 0 1 .4 1 1V20c0 .6-.4 1-1 1A17 17 0 0 1 3 4c0-.6.4-1 1-1h3.5c.6 0 1 .4 1 1 0 1.3.2 2.5.6 3.6.1.3 0 .7-.2 1z"/></svg>07700 318 274</div>
      <div class="row"><svg viewBox="0 0 24 24"><path d="M2 5h20v14H2z M2 5l10 8 10-8"/></svg>info@truelymarvellous.example</div>
    </div>

    <div class="band band--marvellous">
      <svg viewBox="0 0 24 24"><path d="M12 2a10 10 0 1 0 0 20 10 10 0 0 0 0-20zm0 2c.9 1.2 1.6 2.6 2 4h-4c.4-1.4 1.1-2.8 2-4zM4.3 14a8 8 0 0 1 0-4h3.4a16 16 0 0 0 0 4zm5.7 0a14 14 0 0 1 0-4h4a14 14 0 0 1 0 4zm6.3 0a16 16 0 0 0 0-4h3.4a8 8 0 0 1 0 4zM12 20c-.9-1.2-1.6-2.6-2-4h4c-.4 1.4-1.1 2.8-2 4z"/></svg>
      www.truelymarvellous.example
    </div>
    <div class="band band--willow">
      www.ironwillowevents.example
      <svg viewBox="0 0 24 24"><path d="M12 2a10 10 0 1 0 0 20 10 10 0 0 0 0-20zm0 2c.9 1.2 1.6 2.6 2 4h-4c.4-1.4 1.1-2.8 2-4zM4.3 14a8 8 0 0 1 0-4h3.4a16 16 0 0 0 0 4zm5.7 0a14 14 0 0 1 0-4h4a14 14 0 0 1 0 4zm6.3 0a16 16 0 0 0 0-4h3.4a8 8 0 0 1 0 4zM12 20c-.9-1.2-1.6-2.6-2-4h4c-.4 1.4-1.1 2.8-2 4z"/></svg>
    </div>
  </section>

  <section class="card back" aria-label="Card back with both company names">
    <div class="brand brand--marvellous"><span class="dot"></span>Truely Marvellous</div>
    <div class="divider"></div>
    <div class="brand brand--willow"><span class="dot"></span>Iron Willow Events</div>
  </section>
</body>
</html>
```